Flyer for outback tour company

Trifold flyer with a page for each tour that we offer (4 different tours) as well as a front page and a contact page.

Front page: Kestrel Treks logo + an overview of the tours on offer:
- Grand Circuit of the Village and Ridgelands
- Opalvale Showcase Tour
- Twilight Ridgelands Tour
- Subsurface Gemhunt (prospecting) Tour.

Page 2-5: description of each tour with pricing/duration.

Last page (back of brochure): contact details.
Ph: 0488 217 654
E-mail: kestreltreksoz@mailbox-example.net
Online bookings: www.kestreltreksoz-example.com.au.
Tours can also be booked directly through the reception at the Harlow Ridge Desert Lodge and the Clay Nest Inn. Please include the logos for Harlow Ridge and Clay Nest on the last page.

Target Market(s)

Travellers/tourists

Industry/Entity Type

Tourism/tour company

Font styles to use
Sans Serif

Requirements
Must have
• In regards to the pictures… the picture with the tour guide shining the torch should be on the page with the Gemhunt Tour. The other pictures of the cave tunnels should only be on the premium tour/Gemhunt Tour or front/back page.

```html
<!DOCTYPE html>
<html lang="en">
<head>
<meta charset="utf-8">
<title>Kestrel Treks – Trifold Flyer</title>
<link rel="stylesheet" href="https://fonts.googleapis.com/css2?family=Open+Sans:ital,wght@0,400;0,600;0,700;0,800;1,600&display=swap">
<style>
  :root{
    --teal:#2d6b80;
    --teal-dark:#235668;
    --gold:#e2a528;
    --brown:#7b3a1d;
    --rust:#b4562a;
    --sand:#d9a064;
    --paper:#ffffff;
    --ink:#2a3a40;
    --backdrop:#e8e6e3;
  }
  *{box-sizing:border-box;margin:0;padding:0}
  html,body{width:1200px;height:2400px;overflow:hidden;background:var(--backdrop)}
  body{font-family:"Open Sans",Arial,sans-serif;color:var(--ink)}
  .canvas{position:relative;width:1200px;height:2400px}
  .spread{position:absolute;left:30px;width:1140px;height:806px;display:flex;box-shadow:0 6px 24px rgba(0,0,0,.18);background:var(--paper)}
  .spread--outside{top:330px}
  .spread--inside{top:1264px}
  .panel{position:relative;width:380px;height:806px;overflow:hidden}
  .photo{position:absolute}
  .abs{position:absolute}

  /* brand */
  .brand{display:flex;align-items:center;justify-content:center;gap:10px}
  .brand__dot{width:22px;height:22px;border-radius:50%;background:var(--gold)}
  .brand__name{font-weight:800;font-size:34px;color:var(--brown);letter-spacing:.5px;text-transform:uppercase;line-height:1}

  /* type */
  .tour-title{font-weight:800;text-transform:uppercase;line-height:1.2}
  .meta{font-weight:600;font-style:italic;line-height:1.45}
  .body-copy{font-size:12.5px;line-height:1.55}
  .includes-label{font-weight:800;font-size:12.5px;text-transform:uppercase;color:var(--gold);margin:12px 0 6px}
  .steps{list-style:none;counter-reset:step}
  .steps li{counter-increment:step;position:relative;padding-left:26px;font-weight:700;font-size:13px;line-height:1.35;margin-bottom:6px}
  .steps li::before{content:counter(step);position:absolute;left:0;top:0;width:18px;height:18px;border-radius:50%;background:var(--gold);color:#fff;font-size:11px;font-weight:800;text-align:center;line-height:18px}

  /* outside: gemhunt panel */
  .gemhunt{background:var(--teal);color:#fff}
  .gemhunt__text{position:absolute;left:30px;right:30px;top:34px}
  .gemhunt__text .tour-title{font-size:19px;color:var(--gold)}
  .gemhunt__text .meta{font-size:13px;margin:8px 0 10px;color:#fff}
  .gemhunt__text .body-copy{font-size:11.5px;margin-bottom:7px;color:#e8f1f4}

  /* outside: back / contact panel */
  .contact{background:var(--paper)}
  .contact .brand{position:absolute;top:44px;left:0;right:0}
  .contact__lead{position:absolute;top:112px;left:36px;right:36px;text-align:center;font-weight:600;font-style:italic;font-size:15px;line-height:1.4;color:var(--teal-dark)}
  .partners{position:absolute;top:218px;left:0;right:0;display:flex;justify-content:center;gap:40px;align-items:center}
  .partner--lodge{width:74px;height:74px;border-radius:50%;background:var(--rust)}
  .partner--inn{width:96px;height:54px;background:var(--brown)}
  .bookings{position:absolute;top:312px;left:30px;right:30px}
  .bookings__title{text-align:center;font-weight:800;font-size:19px;color:var(--teal);text-transform:uppercase}
  .bookings__url{margin:8px auto 14px;background:var(--teal);color:#fff;font-weight:700;font-size:14px;text-align:center;border-radius:16px;padding:6px 10px}
  .contact-list{list-style:none}
  .contact-list li{display:flex;align-items:flex-start;gap:10px;font-weight:700;font-size:14px;color:var(--teal-dark);margin-bottom:9px;line-height:1.3}
  .contact-list svg{flex:0 0 22px;width:22px;height:22px}

  /* outside: front cover */
  .cover{background:var(--paper)}
  .cover .brand{position:absolute;top:50px;left:0;right:0}
  .cover__overview{position:absolute;left:24px;right:24px;top:604px;text-align:center;color:#fff}
  .cover__overview h2{font-weight:800;font-size:20px;color:var(--gold);text-transform:uppercase;margin-bottom:8px}
  .cover__overview li{list-style:none;font-weight:600;font-size:14.5px;line-height:1.45}
  .cover__url{display:inline-block;margin-top:12px;background:var(--gold);color:var(--teal-dark);font-weight:700;font-size:13.5px;padding:5px 12px}

  /* inside */
  .grand{background:var(--teal);color:#fff}
  .grand__text{position:absolute;left:30px;right:28px;top:34px}
  .grand__text .tour-title{font-size:20px;color:var(--gold)}
  .grand__text .meta{font-size:13.5px;margin:8px 0 10px}
  .grand__text .body-copy{color:#e8f1f4}
  .grand__text .steps li{color:#fff}

  .tour{background:var(--paper)}
  .tour__text{position:absolute;left:32px;right:30px;top:318px}
  .tour__text .tour-title{font-size:20px;color:var(--teal)}
  .tour__text .meta{font-size:13.5px;margin:8px 0 10px;color:var(--teal-dark)}
  .tour__text .steps li{color:var(--teal-dark)}
  .thumbs{position:absolute;left:32px;right:30px;bottom:36px;display:flex;gap:12px}
  .thumb{height:96px;flex:1;border:4px solid #fff;box-shadow:0 2px 6px rgba(0,0,0,.25)}
</style>
</head>
<body>
<main class="canvas">

  <!-- OUTSIDE OF BROCHURE -->
  <section class="spread spread--outside">

    <article class="panel gemhunt">
      <div class="gemhunt__text">
        <h3 class="tour-title">Subsurface Gemhunt (prospecting) Tour</h3>
        <p class="meta">$30<br>Duration approx. 2 hours<br>9.30am start</p>
        <p class="body-copy">This tour is ideal for those who want to try their luck at finding opal the traditional way.</p>
        <p class="body-copy">Guests are taken into a working underground mine where an experienced guide explains how opal forms and where to look.</p>
        <p class="body-copy">Bring a torch and sturdy shoes. Every guest takes home the opal they find, so the adventure keeps going long after the tour ends.</p>
      </div>
      <div class="photo" style="left:30px;top:344px;width:150px;height:92px;border:3px solid #fff;background:linear-gradient(135deg,#6b3a22,#c98a4e 60%,#3d2416)" role="img" aria-label="Hand holding rough opal in a mine tunnel"></div>
      <div class="photo" style="left:192px;top:344px;width:158px;height:92px;border:3px solid #fff;background:linear-gradient(180deg,#7aa6c8 0%,#b9c9d2 45%,#c98648 60%,#8a4a25 100%)" role="img" aria-label="Opal field mullock heaps under a blue sky"></div>
      <div class="photo" style="left:0;top:456px;width:380px;height:350px;background:radial-gradient(ellipse at 45% 40%,#d8d2c6 0%,#8e8273 35%,#4a3a2e 70%,#2a1e17 100%)" role="img" aria-label="Guide shining a torch inside an underground tunnel"></div>
    </article>

    <article class="panel contact">
      <div class="brand"><span class="brand__dot"></span><span class="brand__name">Kestrel Treks</span></div>
      <p class="contact__lead">Tours can also be booked directly through the reception at the Harlow Ridge Desert Lodge and the Clay Nest Inn.</p>
      <div class="partners">
        <div class="partner--inn" role="img" aria-label="Clay Nest Inn badge"></div>
        <div class="partner--lodge" role="img" aria-label="Harlow Ridge Desert Lodge badge"></div>
      </div>
      <div class="bookings">
        <h3 class="bookings__title">Online Bookings</h3>
        <p class="bookings__url">kestreltreksoz-example.com.au</p>
        <ul class="contact-list">
          <li><svg viewBox="0 0 22 22"><circle cx="11" cy="11" r="11" fill="#2d6b80"/><path d="M7.5 6h2l1 2.6-1.3 1a6 6 0 0 0 3.2 3.2l1-1.3 2.6 1v2a1 1 0 0 1-1 1A9 9 0 0 1 6.5 7a1 1 0 0 1 1-1z" fill="#fff"/></svg>0488 217 654</li>
          <li><svg viewBox="0 0 22 22"><circle cx="11" cy="11" r="11" fill="#2d6b80"/><rect x="5.5" y="7" width="11" height="8" fill="#fff"/><path d="M5.5 7l5.5 4.5L16.5 7" fill="none" stroke="#2d6b80" stroke-width="1.2"/></svg>kestreltreksoz@mailbox-example.net</li>
          <li><svg viewBox="0 0 22 22"><circle cx="11" cy="11" r="11" fill="#2d6b80"/><circle cx="11" cy="11" r="5.5" fill="none" stroke="#fff" stroke-width="1.3"/><path d="M5.5 11h11M11 5.5c-2.6 3-2.6 8 0 11M11 5.5c2.6 3 2.6 8 0 11" fill="none" stroke="#fff" stroke-width="1.1"/></svg>www.kestreltreksoz-example.com.au</li>
          <li><svg viewBox="0 0 22 22"><circle cx="11" cy="11" r="11" fill="#2d6b80"/><path d="M11 5a4 4 0 0 1 4 4c0 3-4 8-4 8s-4-5-4-8a4 4 0 0 1 4-4z" fill="#fff"/><circle cx="11" cy="9" r="1.5" fill="#2d6b80"/></svg>Meridian Cross Drive, Opalvale<br>SA 5790, AU</li>
        </ul>
      </div>
      <div class="photo" style="left:0;top:620px;width:380px;height:186px;background:linear-gradient(180deg,#9fb6c4 0%,#d9c6ae 40%,#a9744a 75%,#6e4125 100%)" role="img" aria-label="Rolling outback plains with a winding dirt road"></div>
      <svg class="abs" style="left:0;top:600px" width="380" height="80" viewBox="0 0 380 80">
        <path d="M0 0H380V14C250 60 120 30 0 70Z" fill="#fff"/>
        <path d="M0 70C120 30 250 60 380 14" fill="none" stroke="#e2a528" stroke-width="4"/>
      </svg>
    </article>

    <article class="panel cover">
      <div class="brand"><span class="brand__dot"></span><span class="brand__name">Kestrel Treks</span></div>
      <div class="photo" style="left:0;top:130px;width:380px;height:470px;background:radial-gradient(ellipse at 55% 45%,#c7dbe8 0%,#8fb4cf 28%,#b0612f 45%,#7a3a1d 75%,#4b2412 100%)" role="img" aria-label="View through a desert rock arch to a tour vehicle on red plains"></div>
      <svg class="abs" style="left:0;top:112px" width="380" height="60" viewBox="0 0 380 60">
        <path d="M0 0H380V18C250 40 120 44 0 32Z" fill="#fff"/>
        <path d="M0 32C120 44 250 40 380 18" fill="none" stroke="#e2a528" stroke-width="3"/>
      </svg>
      <svg class="abs" style="left:0;top:520px" width="380" height="286" viewBox="0 0 380 286">
        <path d="M0 80C130 70 260 40 380 0V286H0Z" fill="#2d6b80"/>
        <path d="M0 70C130 60 260 30 380 -10" fill="none" stroke="#e2a528" stroke-width="4"/>
      </svg>
      <div class="cover__overview">
        <h2>Overview of the Tours</h2>
        <ul>
          <li>Grand Circuit of the Village and Ridgelands</li>
          <li>Opalvale Showcase Tour</li>
          <li>Twilight Ridgelands Tour</li>
          <li>Subsurface Gemhunt (prospecting) Tour</li>
        </ul>
        <span class="cover__url">www.kestreltreksoz-example.com.au</span>
      </div>
    </article>
  </section>

  <!-- INSIDE OF BROCHURE -->
  <section class="spread spread--inside">

    <article class="panel grand">
      <div class="grand__text">
        <h3 class="tour-title">Grand Circuit of the Village and the Ridgelands</h3>
        <p class="meta">$99 adults/$75 children<br>Duration approx. 4 hours<br>1pm start</p>
        <p class="body-copy">This tour is designed for those who want a more personal, in-depth experience. Smaller groups, longer stops and local stories from guides who have lived and mined here for decades make it the perfect start.</p>
        <p class="includes-label">The tour includes:</p>
        <ol class="steps">
          <li>The Old Stone Underground Chapel</li>
          <li>Modern Underground Home (Dugout)</li>
          <li>The Moon Plains</li>
          <li>The Dingo Fence</li>
          <li>The Ridgelands</li>
          <li>Underground Mine Tour at our private claim in the opal fields (exclusive to Kestrel Treks)</li>
        </ol>
      </div>
      <div class="photo" style="left:0;top:590px;width:380px;height:216px;background:radial-gradient(ellipse at 50% 35%,#f0c98a 0%,#c98a4c 35%,#8a4a24 70%,#4e2613 100%)" role="img" aria-label="Carved underground chapel interior with painted panels"></div>
      <svg class="abs" style="left:0;top:572px" width="380" height="44" viewBox="0 0 380 44">
        <path d="M0 0H380V8C250 34 120 36 0 22Z" fill="#2d6b80"/>
        <path d="M0 22C120 36 250 34 380 8" fill="none" stroke="#e2a528" stroke-width="3"/>
      </svg>
    </article>

    <article class="panel tour">
      <div class="photo" style="left:0;top:0;width:380px;height:300px;background:linear-gradient(180deg,#2f6fa8 0%,#6fa2c9 35%,#e3b47a 58%,#b8662f 78%,#7a3a1d 100%)" role="img" aria-label="Panorama of colourful desert mesas at dusk"></div>
      <svg class="abs" style="left:0;top:220px" width="380" height="90" viewBox="0 0 380 90">
        <path d="M0 90V70C130 58 260 40 380 14V90Z" fill="#fff"/>
        <path d="M0 70C130 58 260 40 380 14" fill="none" stroke="#e2a528" stroke-width="4"/>
      </svg>
      <div class="tour__text">
        <h3 class="tour-title">Opalvale Showcase Tour</h3>
        <p class="meta">$85 adults/ $59 children<br>Family rate (2 adults and 2 children) $270<br>Duration approx. 3 hours</p>
        <p class="body-copy">A tour that gives you a great insight and introduction into the underground town and the surrounding area.</p>
        <p class="includes-label">The tour includes:</p>
        <ol class="steps">
          <li>Lumora Opal Mine &amp; Museum</li>
          <li>The Old Stone Underground Chapel</li>
          <li>The dingo fence</li>
          <li>The Moon Plains</li>
          <li>The Ridgelands</li>
        </ol>
      </div>
      <div class="thumbs">
        <div class="thumb" style="background:linear-gradient(180deg,#3a4f7a 0%,#c9774a 55%,#2a1a12 100%)" role="img" aria-label="Mining machinery silhouetted at sunset"></div>
        <div class="thumb" style="background:radial-gradient(ellipse at 50% 40%,#e8c27a,#9a5a2c 60%,#4a2614)" role="img" aria-label="Lit interior of an underground church"></div>
      </div>
    </article>

    <article class="panel tour">
      <div class="photo" style="left:0;top:0;width:380px;height:300px;background:linear-gradient(180deg,#2a64a0 0%,#7fb0d4 35%,#e6c08a 56%,#c2743a 78%,#8a4620 100%)" role="img" aria-label="Panorama of colourful desert mesas at dusk"></div>
      <svg class="abs" style="left:0;top:200px" width="380" height="110" viewBox="0 0 380 110">
        <path d="M0 110V14C130 0 260 -10 380 -20V110Z" fill="#fff"/>
        <path d="M0 14C130 0 260 -10 380 -20" fill="none" stroke="#e2a528" stroke-width="4"/>
      </svg>
      <div class="tour__text" style="top:236px">
        <h3 class="tour-title">Twilight Ridgelands Tour</h3>
        <p class="meta">$50<br>Duration approx. 1.5 hours<br>Departs 1 hour before sunset</p>
        <p class="body-copy">A perfect way to end the day. Take in the spectacular views of the Ridgelands as the sun sets and the colours change, while enjoying a light refreshment.</p>
        <p class="includes-label">The tour includes:</p>
        <ol class="steps">
          <li>The Dingo Fence</li>
          <li>The Moon Plains</li>
          <li>The Ridgelands</li>
        </ol>
      </div>
      <div class="thumbs">
        <div class="thumb" style="background:linear-gradient(180deg,#5f8fbf 0%,#dca76a 55%,#8a4a22 100%)" role="img" aria-label="Flat-topped hills glowing at sunset"></div>
        <div class="thumb" style="background:linear-gradient(180deg,#d4885a 0%,#9a5530 50%,#3d2012 100%)" role="img" aria-label="Ridgeline lookout at dusk"></div>
      </div>
    </article>
  </section>

</main>
</body>
</html>
```